Consulting Company PowerPoint Template Design

We are looking for an updated PowerPoint template design or our 55 person energy consulting firm (K7) based in San Francisco (www.kayseven.example). We would like two versions of the same PowerPoint template in a 16:9 and 4:3 format with our existing logo.

We have an existing color scheme and template and are seeking your help to polish/update the template design for wide format and create a flexible template that is easy to use with content from Excel and Word. Our current template, and a couple of examples that we like are attached.

Specific requests include:

• Dark background for slide title
• A narrow section header
• Maximizing white space for content
• A limited number of well designed Master template layouts to choose from
• A selection of title and section header slides that are not San Francisco specific with some variety to chose from ideally with a focus on energy or nature, graphics/visuals.

For examples of energy specific templates see:
https://www.brightslidery.example/energy/powerpoint-templates/0.html

Requirements
Must have
• Must use our logo but open to other designs, fonts, and styles for the PowerPoint template.
• Please use our existing color scheme found in the attached Excel file.
• Also we would like the ability to easily copy and paste from our existing/original template to the new template. In other words we would like backward compatibility to apply the new template format to our old PowerPoints that use our existing template.

```html
<!DOCTYPE html>
<html lang="en">
<head>
<meta charset="utf-8">
<title>K7 Energy Partners – PowerPoint Template</title>
<link rel="stylesheet" href="https://fonts.googleapis.com/css2?family=Roboto+Condensed:wght@700&family=Raleway:wght@300;400&family=Open+Sans:wght@400;700&display=swap">
<style>
  :root{
    --navy:#0e5175;
    --gold:#c9a45c;
    --paper:#ffffff;
    --board:#f4f5f6;
    --ink:#4a4f55;
    --label:#555a60;
    --ring:#e9ebee;
  }
  *{margin:0;padding:0;box-sizing:border-box}
  html,body{width:750px;height:1200px;overflow:hidden;background:var(--board)}
  body{position:relative;font-family:"Open Sans",Arial,sans-serif;color:var(--ink)}

  .slide-frame{position:absolute;overflow:hidden;box-shadow:0 6px 14px rgba(0,0,0,.12)}
  .slide{position:absolute;left:0;top:0;width:417px;height:313px;transform-origin:0 0;background:var(--paper);overflow:hidden}
  .slide--dark{background:var(--navy)}
  .hero{left:115px;top:40px;width:520px;height:390px}
  .hero .slide{transform:scale(1.247)}
  .thumb{width:334px;height:250px}
  .thumb .slide{transform:scale(.801)}
  .pos-a{left:28px;top:521px}.pos-b{left:388px;top:521px}
  .pos-c{left:28px;top:821px}.pos-d{left:388px;top:821px}

  .page-label{position:absolute;width:334px;text-align:center;font-family:"Raleway",sans-serif;font-size:13px;letter-spacing:.5px;color:var(--label)}

  .lines{position:absolute;inset:0}
  .brand{position:absolute;display:flex;align-items:center;font-family:"Roboto Condensed",Arial,sans-serif;font-weight:700;white-space:nowrap}
  .brand-dot{border-radius:50%;flex:none}
  .cover-brand{left:25px;top:24px;gap:14px;font-size:16px;color:#fff}
  .cover-brand .brand-dot{width:34px;height:34px;background:var(--gold)}
  .mini-brand{right:16px;top:20px;gap:4px;font-size:6px;color:var(--navy)}
  .mini-brand .brand-dot{width:12px;height:12px;background:var(--navy)}

  .kicker{position:absolute;left:70px;top:112px;font-family:"Raleway",sans-serif;font-weight:300;font-size:18px;color:var(--gold)}
  .cover-title{position:absolute;left:69px;top:128px;font-family:"Raleway",sans-serif;font-weight:300;font-size:35px;color:#fff;letter-spacing:.5px}

  .heading{position:absolute;font-family:"Raleway",sans-serif;font-weight:300;font-size:19px;line-height:22px;color:var(--navy)}
  .gold{color:var(--gold)}
  .p1-heading{left:15px;top:30px}
  .feature-list{position:absolute;left:16px;top:156px;list-style:none}
  .feature-list li{display:flex;align-items:center;gap:7px;height:25.5px;font-size:6.5px}
  .feature-icon{width:13px;height:13px;border:1px solid #b9c6d0;border-radius:50%;position:relative}
  .feature-icon::after{content:"";position:absolute;left:3.5px;top:3.5px;width:4px;height:4px;background:#9fb3c2;border-radius:1px}
  .screen-fill{position:absolute;left:208px;top:105px;width:209px;height:140px;background:linear-gradient(160deg,#2a2d31 0%,#3d434a 55%,#cfd3d7 92%,#e6e8ea 100%);border-radius:6px 0 0 4px}

  .footer-rule{position:absolute;left:95px;width:227px;top:294px;height:.6px;background:var(--gold);opacity:.7}
  .footer-url{position:absolute;left:0;width:417px;top:290px;text-align:center;font-size:5px;letter-spacing:2.5px;color:var(--gold)}
  .footer-url span{background:var(--paper);padding:0 6px}
  .page-no{position:absolute;right:12px;top:290px;font-size:5px;color:var(--gold)}

  .side-panel{position:absolute;left:283px;top:0;width:134px;height:313px;background:var(--navy)}
  .about-title{left:17px;top:110px}
  .about-copy{position:absolute;left:17px;top:142px;width:235px;font-size:5.3px;line-height:8.2px;text-align:justify}
  .agenda{position:absolute;left:303px;top:24px;list-style:none}
  .agenda li{display:flex;align-items:center;gap:7px;height:44px;font-size:5.8px;color:#fff}
  .agenda b{width:12px;height:12px;border:.8px solid #fff;border-radius:50%;font-weight:400;font-size:5.5px;display:flex;align-items:center;justify-content:center}
  .panel-note{position:absolute;left:295px;top:233px;width:106px;font-size:5.3px;line-height:7px;color:#fff;text-align:justify}
  .page-no--light{color:#fff}
  .footer-url--split span{background:transparent}

  .p3-title{left:15px;top:14px}
  .stat{position:absolute;top:97px;width:110px;text-align:center}
  .stat svg{display:block;margin:0 0 0 10px}
  .stat h3{font-size:6.5px;font-weight:700;color:#333;margin-top:6px}
  .stat p{font-size:6px;line-height:7.5px;margin:2px auto 0;width:80px}

  .site-brand{position:absolute;left:0;width:750px;top:1128px;justify-content:center;gap:14px;font-size:20px;color:var(--navy)}
  .site-brand .brand-dot{width:54px;height:54px;background:var(--navy)}
</style>
</head>
<body>

<!-- Cover, large -->
<div class="slide-frame hero">
  <section class="slide slide--dark">
    <svg class="lines" viewBox="0 0 417 313" aria-hidden="true">
      <g fill="none" stroke-width="3">
        <path d="M372 0V118M372 162V260H77V313" stroke="#fff"/>
        <path d="M0 218H116V295H417" stroke="#c9a45c"/>
      </g>
      <circle cx="373" cy="140" r="14" fill="#c9a45c"/>
    </svg>
    <div class="brand cover-brand"><span class="brand-dot"></span>K7 Energy Partners</div>
    <p class="kicker">POWERPOINT</p>
    <h1 class="cover-title">PRESENTATION</h1>
  </section>
</div>

<!-- Front page -->
<div class="slide-frame thumb pos-a">
  <section class="slide slide--dark">
    <svg class="lines" viewBox="0 0 417 313" aria-hidden="true">
      <g fill="none" stroke-width="2">
        <path d="M372 0V118M372 162V260H77V313" stroke="#fff"/>
        <path d="M0 218H116V295H417" stroke="#c9a45c"/>
      </g>
      <circle cx="373" cy="140" r="14" fill="#c9a45c"/>
    </svg>
    <div class="brand cover-brand"><span class="brand-dot"></span>K7 Energy Partners</div>
    <p class="kicker">POWERPOINT</p>
    <h2 class="cover-title">PRESENTATION</h2>
  </section>
</div>
<p class="page-label" style="left:28px;top:785px">FRONT PAGE</p>

<!-- Page 01 -->
<div class="slide-frame thumb pos-b">
  <section class="slide">
    <div class="brand mini-brand"><span class="brand-dot"></span>K7 Energy Partners</div>
    <h2 class="heading p1-heading">LOREM<br><span class="gold">IPSUM SIMPLY</span><br>TEXT GOES HERE</h2>
    <ul class="feature-list">
      <li><span class="feature-icon"></span>Lorem ipsum is a simply dummy text</li>
      <li><span class="feature-icon"></span>Lorem ipsum is a simply dummy text</li>
      <li><span class="feature-icon"></span>Lorem ipsum is a simply dummy text</li>
      <li><span class="feature-icon"></span>Lorem ipsum is a simply dummy text</li>
    </ul>
    <div class="screen-fill" role="img" aria-label="Laptop showing a grid of energy service tiles"></div>
    <div class="footer-rule"></div>
    <p class="footer-url"><span>www.kayseven.example</span></p>
    <p class="page-no">01</p>
  </section>
</div>
<p class="page-label" style="left:388px;top:785px">PAGE - 01</p>

<!-- Page 02 -->
<div class="slide-frame thumb pos-c">
  <section class="slide">
    <div class="side-panel"></div>
    <h2 class="heading about-title"><span class="gold">ABOUT</span> US</h2>
    <p class="about-copy">Lorem Ipsum is simply dummy text of the printing and typesetting industry. Lorem Ipsum has been the industry's standard dummy text ever since the 1500s, when an unknown printer took a galley of type and scrambled it to make a type specimen book. It has survived not only five centuries, but also the leap into electronic typesetting, remaining essentially unchanged.</p>
    <ol class="agenda">
      <li><b>1</b>Lorem ipsum simply text</li>
      <li><b>2</b>Lorem ipsum simply text</li>
      <li><b>3</b>Lorem ipsum simply text</li>
      <li><b>4</b>Lorem ipsum simply text</li>
      <li><b>5</b>Lorem ipsum simply text</li>
    </ol>
    <p class="panel-note">Lorem Ipsum is simply dummy text of the printing &amp; typesetting industry.</p>
    <div class="footer-rule" style="width:188px"></div>
    <p class="footer-url footer-url--split" style="width:283px"><span style="background:var(--paper)">www.kayseven.example</span></p>
    <p class="page-no page-no--light">02</p>
  </section>
</div>
<p class="page-label" style="left:28px;top:1085px">PAGE - 02</p>

<!-- Page 03 -->
<div class="slide-frame thumb pos-d">
  <section class="slide">
    <h2 class="heading p3-title"><span class="gold">LOREM</span> IPSUM</h2>
    <div class="brand mini-brand"><span class="brand-dot"></span>K7 Energy Partners</div>

    <div class="stat" style="left:4px">
      <svg width="90" height="70" viewBox="0 0 90 70" aria-hidden="true">
        <circle cx="35" cy="35" r="30" fill="none" stroke="var(--ring)" stroke-width="5"/>
        <circle cx="35" cy="35" r="30" fill="none" stroke="var(--gold)" stroke-width="5" pathLength="100" stroke-dasharray="25 75" transform="rotate(-90 35 35)"/>
        <circle cx="67" cy="27" r="12" fill="var(--navy)"/>
        <text x="67" y="30.5" text-anchor="middle" font-family="Open Sans,sans-serif" font-weight="700" font-size="10" fill="#fff">50</text>
      </svg>
      <h3>TEXT HERE</h3>
      <p>Lorem Ipsum is simply dummy text of the printing and typesetting industry.</p>
    </div>

    <div class="stat" style="left:158px">
      <svg width="90" height="70" viewBox="0 0 90 70" aria-hidden="true">
        <circle cx="35" cy="35" r="30" fill="none" stroke="var(--ring)" stroke-width="5"/>
        <circle cx="35" cy="35" r="30" fill="none" stroke="var(--gold)" stroke-width="5" pathLength="100" stroke-dasharray="25 75" transform="rotate(-90 35 35)"/>
        <circle cx="67" cy="27" r="12" fill="var(--navy)"/>
        <text x="67" y="30.5" text-anchor="middle" font-family="Open Sans,sans-serif" font-weight="700" font-size="10" fill="#fff">30</text>
      </svg>
      <h3>TEXT HERE</h3>
      <p>Lorem Ipsum is simply dummy text of the printing and typesetting industry.</p>
    </div>

    <div class="stat" style="left:308px">
      <svg width="90" height="70" viewBox="0 0 90 70" aria-hidden="true">
        <circle cx="35" cy="35" r="30" fill="none" stroke="var(--ring)" stroke-width="5"/>
        <circle cx="35" cy="35" r="30" fill="none" stroke="var(--gold)" stroke-width="5" pathLength="100" stroke-dasharray="25 75" transform="rotate(-90 35 35)"/>
        <circle cx="67" cy="27" r="12" fill="var(--navy)"/>
        <text x="67" y="30.5" text-anchor="middle" font-family="Open Sans,sans-serif" font-weight="700" font-size="10" fill="#fff">10</text>
      </svg>
      <h3>TEXT HERE</h3>
      <p>Lorem Ipsum is simply dummy text of the printing and typesetting industry.</p>
    </div>

    <div class="footer-rule"></div>
    <p class="footer-url"><span>www.kayseven.example</span></p>
    <p class="page-no">03</p>
  </section>
</div>
<p class="page-label" style="left:388px;top:1085px">PAGE - 03</p>

<div class="brand site-brand"><span class="brand-dot"></span>K7 Energy Partners</div>

</body>
</html>
```